Brevin Law Client Handbook

We are a small, rapidly growing, criminal defense law firm located in a suburb of Seattle, WA. The cover should be professional and be consistent with our image a sleek, modern, and efficient. The included files show our designs used in other projects for reference.

```html
<!DOCTYPE html>
<html lang="en">
<head>
<meta charset="UTF-8">
<title>Brevin Law Firm — Client Handbook Cover</title>
<link rel="stylesheet" href="https://fonts.googleapis.com/css2?family=Cinzel:wght@400;500&family=Montserrat:wght@500&display=swap">
<style>
  :root {
    --stage: #3f5a7c;
    --navy-deep: #14305a;
    --navy-mid: #1c4a80;
    --navy-stripe: #1d3f70;
    --paper: #ffffff;
    --ink: #1a2a44;
    --photo-light: #c9ced4;
    --photo-dark: #3a414b;
  }
  * { margin: 0; padding: 0; box-sizing: border-box; }
  html, body {
    width: 1200px; height: 663px; overflow: hidden;
    background: var(--stage);
  }
  .stage {
    width: 1200px; height: 663px;
    display: flex; align-items: center; justify-content: center;
  }
  .cover {
    position: relative;
    width: 438px; height: 620px;
    background: var(--paper);
    box-shadow: 0 10px 30px rgba(0,0,0,.35);
    overflow: hidden;
  }
  .cover__photo {
    position: absolute; left: 0; top: 0;
    width: 438px; height: 323px;
    background: linear-gradient(160deg, var(--photo-light) 0%, #9aa2ac 45%, var(--photo-dark) 100%);
  }
  .cover__chevron {
    position: absolute; left: 0; top: 0;
    width: 438px; height: 110px;
  }
  .cover__url {
    position: absolute; top: 20px; left: 0; width: 100%;
    text-align: center;
    font-family: "Montserrat", sans-serif; font-weight: 500;
    font-size: 7.5px; letter-spacing: .38em; color: var(--ink);
  }
  .cover__panel {
    position: absolute; left: 0; top: 331px;
    width: 438px; height: 224px;
    background: linear-gradient(90deg, var(--navy-deep) 0%, var(--navy-mid) 55%, var(--navy-deep) 100%);
    color: var(--paper);
    text-align: center;
  }
  .brand {
    display: flex; align-items: center; justify-content: center; gap: 8px;
    margin-top: 40px;
    font-family: "Cinzel", serif; font-weight: 400;
    font-size: 17px; letter-spacing: .18em;
  }
  .brand__square { width: 18px; height: 18px; background: var(--paper); }
  .title {
    font-family: "Cinzel", serif; font-weight: 500;
    line-height: 1;
    text-shadow: 0 1px 2px rgba(0,0,0,.35);
  }
  .title__line1 { display: block; margin-top: 26px; font-size: 50px; letter-spacing: .14em; padding-left: .14em; }
  .title__line2 { display: block; margin-top: 2px; font-size: 49px; letter-spacing: .01em; }
  .cover__author {
    position: absolute; left: 0; top: 555px;
    width: 438px; height: 49px;
    display: flex; align-items: center; justify-content: center;
    font-family: "Montserrat", sans-serif; font-weight: 500;
    font-size: 12px; letter-spacing: .42em; color: var(--ink);
    background: var(--paper);
  }
  .cover__base {
    position: absolute; left: 0; top: 604px;
    width: 438px; height: 16px;
    background: var(--navy-deep);
  }
</style>
</head>
<body>
<main class="stage">
  <article class="cover">
    <div class="cover__photo" role="img" aria-label="Black and white photo of brass scales of justice and a wooden gavel on a desk"></div>
    <svg class="cover__chevron" viewBox="0 0 438 110" aria-hidden="true">
      <polygon points="0,0 438,0 438,22 219,110 0,22" fill="var(--navy-stripe)"/>
      <polygon points="0,0 438,0 438,14 219,100 0,14" fill="var(--paper)"/>
      <polygon points="0,0 438,0 438,10 219,94 0,10" fill="var(--navy-stripe)"/>
      <polygon points="0,0 438,0 438,4 219,87 0,4" fill="var(--paper)"/>
    </svg>
    <p class="cover__url">WWW.BREVINLAWFIRM.COM</p>
    <section class="cover__panel">
      <div class="brand"><span class="brand__square"></span>BREVIN LAW FIRM</div>
      <h1 class="title">
        <span class="title__line1">CLIENT</span>
        <span class="title__line2">HANDBOOK</span>
      </h1>
    </section>
    <p class="cover__author">AUTHOR NAME</p>
    <div class="cover__base"></div>
  </article>
</main>
</body>
</html>
```